Leuchtkasten für Pflegedienst
Zielgruppe
Wir sind ein ambulnter Pflegedienst in Rostock. Derzeit befindet sich am Haus ein runder Leuchtkasten mit dem alten Logo. Das Logo wurde erneuert. Nun soll der Leuchtkasten mit einem Durchmessr von 80 cm neu gestaltet werden.
Aufgabenstellung
bitte zwei unterscheideliche Entwürfe für die Vorder und die Rückseite. Es sollte auf der einen Seite vielleicht das Logo anthalten sein und auf der anderen Seite eine andere kreative Idee. Hauskrankenpflege Sorgenhaus Linde sollten enthalten sein, sowie die Telefonummer 0381-52946138
Auf der anderen Seite wurde ein Schriftzug in Edelstahl rostoptik montiert.
Wichtig ist, dass das der ENtwurf auf einer durchleichtbaren Folie gedruckt werden kann.
Der KAffee slogan war füe eine andere Aktion und sollte nicht auf den Leuchtkasten.

```html
<!DOCTYPE html>
<html lang="de">
<head>
<meta charset="utf-8">
<title>Sorgenhaus Linde – Leuchtkasten Vorder- und Rückseite</title>
<link rel="stylesheet" href="https://fonts.googleapis.com/css2?family=Fira+Sans:wght@700&display=swap">
<style>
  :root {
    --navy: #161d33;
    --teal: #5dbba6;
    --white: #ffffff;
    --paper: #ffffff;
  }
  html, body {
    margin: 0;
    padding: 0;
    width: 1200px;
    height: 1106px;
    overflow: hidden;
    background: var(--paper);
  }
  .sheet {
    position: relative;
    width: 1200px;
    height: 1106px;
    display: flex;
    align-items: center;
    justify-content: center;
    gap: 50px;
  }
  .lightbox-face {
    width: 500px;
    height: 500px;
    display: block;
  }
  .face-bg { fill: var(--navy); }
  .phone-band { fill: var(--teal); }
  .brand-ring {
    fill: none;
    stroke: var(--white);
    stroke-width: 8;
  }
  .brand-name,
  .phone-number,
  .service-ring-text {
    font-family: "Fira Sans", Arial, sans-serif;
    font-weight: 700;
  }
  .brand-name {
    fill: var(--white);
    text-anchor: middle;
  }
  .phone-number {
    fill: var(--white);
    font-size: 36px;
  }
  .service-ring-text { font-size: 33px; }
  .service-teal { fill: var(--teal); }
  .service-white { fill: var(--white); }
</style>
</head>
<body>
<main class="sheet">

  <!-- Front face: name and phone -->
  <svg class="lightbox-face lightbox-front" viewBox="0 0 500 500" aria-label="Vorderseite Sorgenhaus Linde">
    <defs>
      <clipPath id="front-disc">
        <circle cx="250" cy="250" r="250"/>
      </clipPath>
    </defs>
    <g clip-path="url(#front-disc)">
      <rect class="face-bg" x="0" y="0" width="500" height="500"/>
      <path class="phone-band" d="M0,278 C120,360 260,415 510,412 L510,510 L0,510 Z"/>
    </g>
    <circle class="brand-ring" cx="250" cy="116" r="84"/>
    <text class="brand-name" x="250" y="262" font-size="60">Sorgenhaus</text>
    <text class="brand-name" x="250" y="328" font-size="60">Linde</text>
    <text class="phone-number" x="78" y="365" transform="rotate(21 78 365)">0381-52946138</text>
  </svg>

  <!-- Back face: ring of service text -->
  <svg class="lightbox-face lightbox-back" viewBox="0 0 500 500" aria-label="Rückseite Hauskrankenpflege Sorgenhaus Linde">
    <defs>
      <path id="service-ring-path" d="M250,250 m-203,0 a203,203 0 1,1 406,0 a203,203 0 1,1 -406,0"/>
    </defs>
    <circle class="face-bg" cx="250" cy="250" r="250"/>
    <text class="service-ring-text">
      <textPath href="#service-ring-path" textLength="1270" lengthAdjust="spacing">
        <tspan class="service-teal">Hauskrankenpflege</tspan><tspan class="service-white"> • Hauskrankenpflege • </tspan><tspan class="service-teal">Hauskrankenpflege</tspan><tspan class="service-white"> • Hauskrankenpflege •</tspan>
      </textPath>
    </text>
    <circle class="brand-ring" cx="250" cy="250" r="148" stroke-width="10"/>
    <text class="brand-name" x="250" y="240" font-size="48">Sorgenhaus</text>
    <text class="brand-name" x="250" y="296" font-size="48">Linde</text>
  </svg>

</main>
</body>
</html>
```